Coffee cup sleeve design

Need a coffee cup sleeve designed. I've included our logo as well as some inspiration photos and the template for the sleeve. Would like to add a very small 8pt "Lamentations 3:22-23" on back too.

Colors

Designer to choose only greyscale colors for use in the design.

```html
<!DOCTYPE html>
<html lang="en">
<head>
<meta charset="utf-8">
<title>Northpine Cafe – Cup Sleeve</title>
<link href="https://fonts.googleapis.com/css2?family=Marcellus&family=Dancing+Script:wght@600;700&family=Fredoka:wght@600&family=Open+Sans:wght@700&display=swap" rel="stylesheet">
<style>
  :root{
    --page:#efefef;
    --sleeve:#f6f6f6;
    --ink:#1f1f1f;
    --ink-soft:#3a3a3a;
    --ray-dark:#2b2b2b;
    --ray-light:#ececec;
    --paper:#ffffff;
  }
  *{box-sizing:border-box;margin:0;padding:0}
  html,body{width:800px;height:1200px;overflow:hidden;background:var(--page)}
  .canvas{position:relative;width:800px;height:1200px}
  .sleeve{
    position:absolute;left:60px;width:680px;height:470px;
    background:var(--sleeve);
    box-shadow:0 2px 10px rgba(0,0,0,.08);
    overflow:hidden;
  }
  .sleeve--front{top:50px}
  .sleeve--back{top:660px}
  .name-strip{
    position:absolute;left:0;right:0;height:36px;
    display:flex;justify-content:space-around;align-items:center;
    background:var(--paper);
    font-family:"Marcellus",serif;font-size:19px;color:var(--ink);
    letter-spacing:.5px;white-space:nowrap;overflow:hidden;
  }
  .name-strip--top{top:0;border-bottom:1px solid #ddd}
  .name-strip--bottom{bottom:0;border-top:1px solid #ddd}
  .rays{
    position:absolute;left:0;right:0;top:36px;bottom:36px;
    background:radial-gradient(circle at 50% 50%, var(--ray-light) 0 24%, #9a9a9a 42%, var(--ray-dark) 100%);
  }
  .quote{
    position:absolute;left:50%;top:50%;transform:translate(-50%,-50%);
    width:300px;padding:20px 10px;text-align:center;color:var(--ink-soft);
  }
  .quote__lead{font-family:"Dancing Script",cursive;font-weight:600;font-size:50px;line-height:1}
  .quote__the{font-family:"Fredoka",sans-serif;font-size:34px;line-height:1.05}
  .quote__main{font-family:"Fredoka",sans-serif;font-size:46px;line-height:1.05}
  .quote__end{font-family:"Dancing Script",cursive;font-weight:700;font-size:76px;line-height:.95}
  .brand-name{
    position:absolute;left:50%;top:50%;transform:translate(-50%,-50%);
    font-family:"Marcellus",serif;font-size:30px;color:var(--ink);
    letter-spacing:1px;white-space:nowrap;
  }
  .verse-bar{
    position:absolute;left:14px;top:36px;bottom:36px;width:34px;
    background:var(--ink);
    display:flex;align-items:center;justify-content:center;
  }
  .verse-bar__text{
    transform:rotate(90deg);white-space:nowrap;
    font-family:"Open Sans",sans-serif;font-weight:700;font-size:11px;color:var(--paper);
  }
</style>
</head>
<body>
<main class="canvas">
  <section class="sleeve sleeve--front">
    <div class="name-strip name-strip--top"><span>NORTHPINE CAFE</span><span>NORTHPINE CAFE</span><span>NORTHPINE CAFE</span></div>
    <div class="rays" role="img" aria-label="Distressed black sunburst rays radiating from the centre"></div>
    <div class="quote">
      <p class="quote__lead">And now</p>
      <p class="quote__the">THE</p>
      <p class="quote__main">Adventure</p>
      <p class="quote__end">begins</p>
    </div>
    <div class="name-strip name-strip--bottom"><span>NORTHPINE CAFE</span><span>NORTHPINE CAFE</span><span>NORTHPINE CAFE</span></div>
  </section>

  <section class="sleeve sleeve--back">
    <div class="name-strip name-strip--top"><span>NORTHPINE CAFE</span><span>NORTHPINE CAFE</span><span>NORTHPINE CAFE</span></div>
    <div class="rays" role="img" aria-label="Distressed black sunburst rays radiating from the centre"></div>
    <div class="verse-bar"><span class="verse-bar__text">Lamentations 3:22-23</span></div>
    <p class="brand-name">NORTHPINE CAFE</p>
    <div class="name-strip name-strip--bottom"><span>NORTHPINE CAFE</span><span>NORTHPINE CAFE</span><span>NORTHPINE CAFE</span></div>
  </section>
</main>
</body>
</html>
```